Seven nights at the harbour

Creation of the cover for the book: "Sept nuits sur le quai du port" with the joined photo of a 70 years old lady.
Title: "Seven nights along the old harbour"
Author: "Mireille Vaston"
Publisher: "Editions Morvane" (should be at the bottom of the page)
Format: 14 x 20.5 cm
The story: A senior lady (70 years old), divorced, with a beautiful face, still wants to seduce, even young men.
We found the perfect photo for the woman. We would like to ask you to make a modern cover from it.
Besoin de quelques jours pour choisir un design
Target Market(s)
Novels reader (adults)
Industry/Entity Type
book

```html
<!DOCTYPE html>
<html lang="en">
<head>
<meta charset="utf-8">
<title>Seven nights along the old harbour — cover</title>
<link href="https://fonts.googleapis.com/css2?family=Bebas+Neue&family=Oswald:wght@500;700&family=Dancing+Script:wght@700&display=swap" rel="stylesheet">
<style>
  :root {
    --page: #ffffff;
    --ink-dark: #0f1016;
    --title-pink: #ff2f6e;
    --title-pink-light: #ffb3c6;
    --script-white: #ffffff;
    --script-outline: #000000;
    --publisher: #ffffff;
    --author: #ffffff;
    --photo-orange: #d8741c;
    --photo-red: #e8262b;
    --photo-pink: #f23a63;
    --photo-plum: #6a1436;
    --photo-navy: #1d1a3a;
    --photo-blue: #2b5e9c;
    --photo-silver: #d9d9dc;
  }
  * { margin: 0; padding: 0; box-sizing: border-box; }
  html, body {
    width: 1200px; height: 1000px; overflow: hidden;
    background: var(--page);
  }
  .stage { position: relative; width: 1200px; height: 1000px; }

  .cover {
    position: absolute; left: 296px; top: 54px;
    width: 609px; height: 891px; overflow: hidden;
    background: var(--ink-dark);
  }

  .cover-photo {
    position: absolute; inset: 0;
    background:
      radial-gradient(ellipse 55% 30% at 80% 12%, var(--photo-silver) 0%, rgba(217,217,220,0) 70%),
      radial-gradient(ellipse 50% 35% at 12% 35%, var(--photo-orange) 0%, rgba(216,116,28,0) 75%),
      radial-gradient(ellipse 60% 40% at 55% 45%, var(--photo-red) 0%, rgba(232,38,43,0) 75%),
      radial-gradient(ellipse 45% 30% at 85% 40%, var(--photo-pink) 0%, rgba(242,58,99,0) 80%),
      radial-gradient(ellipse 45% 25% at 95% 95%, var(--photo-blue) 0%, rgba(43,94,156,0) 80%),
      linear-gradient(180deg, #c8322c 0%, var(--photo-plum) 58%, var(--photo-navy) 75%, var(--ink-dark) 100%);
  }

  .band { position: absolute; }
  .band--top-block { top: 0; left: 0; width: 372px; height: 132px; background: rgba(240, 40, 80, 0.85); }
  .band--lower { top: 680px; left: 0; width: 100%; height: 211px; background: rgba(10, 12, 24, 0.45); }

  .numeral {
    position: absolute; left: -95px; top: -150px;
    font-family: "Oswald", sans-serif; font-weight: 700;
    font-size: 760px; line-height: 1;
    color: rgba(40, 6, 18, 0.45);
    mix-blend-mode: multiply;
  }

  .author {
    position: absolute; left: 0; top: 50px; width: 372px;
    text-align: center;
    font-family: "Oswald", sans-serif; font-weight: 500;
    font-size: 24px; line-height: 1; letter-spacing: 6px;
    text-transform: uppercase;
    color: var(--author);
  }

  .title { position: absolute; inset: 0; font-weight: normal; }
  .title-line {
    position: absolute; left: 0; width: 100%;
    text-align: center; white-space: nowrap;
    font-family: "Bebas Neue", sans-serif;
    line-height: 1;
    background: linear-gradient(180deg, var(--title-pink-light) 0%, var(--title-pink) 60%);
    -webkit-background-clip: text; background-clip: text;
    color: transparent;
  }
  .title-line--first { top: 536px; font-size: 74px; letter-spacing: 1px; }
  .title-line--last { top: 668px; font-size: 124px; letter-spacing: 2px; }
  .title-script {
    position: absolute; left: 50%; top: 600px;
    transform: translateX(-50%) rotate(-8deg);
    font-family: "Dancing Script", cursive; font-weight: 700;
    font-size: 104px; line-height: 1;
    color: var(--script-white);
    -webkit-text-stroke: 4px var(--script-outline);
    paint-order: stroke fill;
  }

  .publisher {
    position: absolute; left: 0; top: 818px; width: 100%;
    text-align: center;
    font-family: "Oswald", sans-serif; font-weight: 500;
    font-size: 22px; line-height: 1; letter-spacing: 7px;
    text-transform: uppercase;
    color: var(--publisher);
  }
</style>
</head>
<body>
<div class="stage">
  <section class="cover">
    <div class="cover-photo" role="img" aria-label="Photo of a 70-year-old woman, her face veiled by long strands of dyed hair in red, orange, pink, silver and blue"></div>
    <div class="band band--top-block"></div>
    <div class="band band--lower"></div>
    <div class="numeral" aria-hidden="true">7</div>

    <p class="author">Mireille Vaston</p>

    <h1 class="title">
      <span class="title-line title-line--first">Seven nights along</span>
      <span class="title-line title-line--last">The harbour</span>
      <span class="title-script">old</span>
    </h1>

    <p class="publisher">Editions Morvane</p>
  </section>
</div>
</body>
</html>
```